" Venda de planos de assistência familiar oferecendo uma rede descontos e funerais para os seus associados ; Serviços funerários; Venda de coroa de flores e arranjos. "

```html
<!DOCTYPE html>
<html lang="pt-BR">
<head>
<meta charset="UTF-8">
<title>Plano Aurora – Carnê de Pagamento</title>
<link href="https://fonts.googleapis.com/css2?family=Montserrat:wght@400;600;700;800&display=swap" rel="stylesheet">
<style>
  :root{
    --teal:#1f8a7e;
    --teal-dark:#187569;
    --teal-light:#4fc3b8;
    --white:#ffffff;
    --paper:#fbfbfb;
    --ink:#4a4a4a;
    --faint:#e6e6e6;
    --accent-red:#d9302f;
    --stage:#e8e4dd;
  }
  *{box-sizing:border-box;margin:0;padding:0}
  html,body{width:1200px;height:1200px;overflow:hidden}
  body{background:var(--stage);font-family:'Montserrat',sans-serif;position:relative}

  .cover{position:absolute;left:0;top:235px;width:1200px;height:394px;background:var(--teal);overflow:hidden}
  .cover-sidebar{position:absolute;left:0;top:0;width:150px;height:100%;background:var(--teal-dark);
    display:flex;flex-direction:column;align-items:center;padding-top:48px;gap:26px;color:var(--white);text-align:center}
  .sidebar-brand{display:flex;flex-direction:column;align-items:center;gap:8px;font-weight:700;font-size:14px;line-height:1.15}
  .brand-dot{width:34px;height:34px;border:2px solid var(--white);border-radius:50%}
  .admin-label{font-weight:700;font-size:14px;line-height:1.2}
  .admin-brand{display:flex;align-items:center;gap:6px;font-weight:700;font-size:12px}
  .admin-square{width:26px;height:26px;background:var(--accent-red)}

  .cover-logo{position:absolute;left:360px;top:40px;width:440px;display:flex;flex-direction:column;align-items:center;color:var(--white)}
  .logo-circle{width:120px;height:120px;border:4px solid var(--white);border-radius:50%;margin-bottom:26px}
  .logo-name{font-weight:800;font-size:46px;letter-spacing:1px;line-height:1}
  .logo-tagline{margin-top:10px;padding-top:6px;border-top:1px solid rgba(255,255,255,.7);font-size:10px;font-weight:600;letter-spacing:1.5px}
  .cover-title{margin-top:30px;font-weight:700;font-size:24px}

  .cover-decor{position:absolute;right:0;top:0;width:320px;height:100%;
    background:radial-gradient(circle at 70% 40%,rgba(255,255,255,.35),rgba(79,195,184,.25) 45%,rgba(31,138,126,0) 75%)}

  .back{position:absolute;left:0;top:660px;width:1200px;height:390px;background:var(--paper);overflow:hidden}
  .back-decor{position:absolute;left:440px;top:0;width:280px;height:300px;
    background:radial-gradient(ellipse at 50% 45%,var(--faint),rgba(230,230,230,0) 70%)}
  .footer-rule{position:absolute;left:290px;right:200px;top:288px;height:3px;background:var(--teal)}
  .contacts{position:absolute;left:60px;right:40px;top:330px;display:flex;align-items:center;gap:34px;font-size:11.5px;color:var(--ink)}
  .contact{display:flex;align-items:center;gap:8px;white-space:nowrap}
  .contact svg{flex:none}
  .social-dot{width:18px;height:18px;border:2px solid var(--teal);border-radius:50%}
  .footer-band{position:absolute;left:0;right:0;bottom:0;height:22px;background:var(--teal)}
</style>
</head>
<body>
  <section class="cover">
    <aside class="cover-sidebar">
      <div class="sidebar-brand"><span class="brand-dot"></span>Jardim<br>Sereno</div>
      <svg class="hours-icon" width="50" height="50" viewBox="0 0 50 50" aria-label="24 horas">
        <path d="M40 12 A19 19 0 1 0 44 25" fill="none" stroke="#fff" stroke-width="3"/>
        <path d="M34 10 L41 11 L40 18" fill="none" stroke="#fff" stroke-width="3"/>
        <text x="25" y="28" fill="#fff" font-family="Montserrat,sans-serif" font-weight="800" font-size="14" text-anchor="middle">24</text>
        <text x="25" y="37" fill="#fff" font-family="Montserrat,sans-serif" font-size="6" text-anchor="middle">Horas</text>
      </svg>
      <div>
        <p class="admin-label">Administrado<br>por:</p>
        <div class="admin-brand" style="margin-top:12px"><span class="admin-square"></span>Gestora Norte</div>
      </div>
    </aside>

    <div class="cover-logo">
      <span class="logo-circle"></span>
      <h1 class="logo-name">PLANO AURORA</h1>
      <p class="logo-tagline">PLANO ASSISTENCIAL JARDIM SERENO</p>
      <h2 class="cover-title">Carnê de Pagamento</h2>
    </div>

    <div class="cover-decor" role="img" aria-label="Grande símbolo decorativo de árvore em linhas brancas e turquesa"></div>
  </section>

  <section class="back">
    <div class="back-decor" role="img" aria-label="Símbolo de árvore em cinza claro como marca d'água"></div>
    <div class="footer-rule"></div>
    <div class="contacts">
      <span class="contact">
        <svg width="16" height="16" viewBox="0 0 24 24"><path d="M6 2 L10 6 L7.5 9 C9 12.5 11.5 15 15 16.5 L18 14 L22 18 L19 22 C10 21 3 14 2 5 Z" fill="var(--teal)"/></svg>
        00 0000-0000 | 00 000000-0000
      </span>
      <span class="contact">00 0000-0000 | 00 000000-0000</span>
      <span class="contact">
        <svg width="18" height="14" viewBox="0 0 18 14"><rect x="1" y="1" width="16" height="12" fill="none" stroke="var(--teal)" stroke-width="1.6"/><path d="M1 1 L9 8 L17 1" fill="none" stroke="var(--teal)" stroke-width="1.6"/></svg>
        contato@planoaurora.com.br
      </span>
      <span class="contact">
        <svg width="18" height="14" viewBox="0 0 18 14"><rect x="1" y="1" width="16" height="12" fill="none" stroke="var(--teal)" stroke-width="1.6"/><path d="M1 1 L9 8 L17 1" fill="none" stroke="var(--teal)" stroke-width="1.6"/></svg>
        contato@planoaurora.com.br
      </span>
      <span class="contact"><span class="social-dot"></span>planoaurora</span>
    </div>
    <div class="footer-band"></div>
  </section>
</body>
</html>
```